School teacher strategies for teachers to improve their lessons.

This is for displays for teachers in their office about how to best teach students. This should be styled in a professional way that aligns with the colour themes of the school.

For reference, here is the school's website:
https://talvingrovehs.norvale-learn.edu.au/

I have attached a previous document "Steady Practices" - please use similar theme.

Target Market(s)

teachers at this school

Colors

Requirements
Must have
• School logo. And aligned to previous designs

```html
<!DOCTYPE html>
<html lang="en">
<head>
<meta charset="utf-8">
<title>Talvin Grove Instructional Model – Learning Goal &amp; Success Criteria</title>
<link href="https://fonts.googleapis.com/css2?family=Archivo:wght@700;800&family=Arimo:wght@400;700&display=swap" rel="stylesheet">
<style>
  :root {
    --school-blue: #253f8f;
    --school-yellow: #f0e05a;
    --paper: #ffffff;
    --ink: #111111;
    --heading-font: "Archivo", Verdana, sans-serif;
    --body-font: "Arimo", Arial, sans-serif;
  }
  * { box-sizing: border-box; margin: 0; padding: 0; }
  html, body { width: 929px; height: 1200px; overflow: hidden; background: var(--paper); }
  body { position: relative; font-family: var(--body-font); color: var(--ink); }

  .block { position: absolute; }
  .rounded { border-radius: 18px; }
  .blue { background: var(--school-blue); color: var(--paper); }
  .yellow { background: var(--school-yellow); }

  /* masthead */
  .masthead-left { left: 29px; top: 25px; width: 395px; height: 106px; border-radius: 18px 0 0 18px; }
  .masthead-right { left: 506px; top: 25px; width: 397px; height: 106px; border-radius: 0 18px 18px 0; }
  .school-name {
    position: absolute; left: 424px; top: 25px; width: 82px; height: 106px;
    display: flex; align-items: center; justify-content: center; text-align: center;
    font-family: var(--heading-font); font-weight: 800; font-size: 17px; line-height: 1.15;
    color: var(--school-blue);
  }

  .title-bar {
    left: 29px; width: 874px; display: flex; align-items: center; justify-content: center;
    font-family: var(--heading-font); font-weight: 800; color: var(--paper); border-radius: 20px;
  }
  .title-main { top: 138px; height: 54px; font-size: 25px; letter-spacing: 0.3px; }
  .title-sub { top: 199px; height: 54px; font-size: 24px; }

  .purpose { left: 0; width: 929px; top: 262px; text-align: center; font-size: 13px; }
  .formula-label {
    left: 0; width: 929px; top: 281px; text-align: center;
    font-family: var(--heading-font); font-weight: 800; font-size: 17px; color: var(--school-yellow);
  }
  .formula {
    left: 29px; top: 310px; width: 874px; height: 33px; border-radius: 17px;
    display: flex; align-items: center; justify-content: center;
    font-family: var(--heading-font); font-weight: 800; font-size: 15px; color: var(--paper);
  }

  .card { padding: 10px 20px; }
  .card-heading {
    text-align: center; font-family: var(--heading-font); font-weight: 800;
    font-size: 16px; color: var(--paper); margin-bottom: 6px;
  }
  .card p { font-size: 13.5px; line-height: 1.4; text-indent: 22px; }
  .example-left { left: 29px; top: 352px; width: 427px; height: 109px; }
  .example-right { left: 475px; top: 352px; width: 426px; height: 109px; padding-top: 6px; }

  .section-bar {
    left: 25px; width: 875px; height: 44px; border-radius: 18px;
    display: flex; align-items: center; justify-content: center;
    font-family: var(--heading-font); font-weight: 800; font-size: 20px; color: var(--paper);
  }
  .essentials-bar { top: 470px; }
  .criteria-bar { left: 26px; width: 874px; top: 727px; }

  .checklist {
    left: 25px; top: 522px; width: 875px; height: 196px; border-radius: 16px;
    padding: 10px 24px 0 28px; list-style: none; font-size: 13.5px; line-height: 1.9;
  }
  .checklist li::before { content: "•"; margin-right: 8px; }

  .criteria-intro { left: 40px; width: 849px; top: 782px; text-align: center; font-size: 13.5px; line-height: 1.35; }

  .criteria-card { top: 828px; height: 202px; padding: 12px 18px; }
  .criteria-card ul { list-style: none; font-size: 13.5px; line-height: 1.4; }
  .criteria-card li { margin-bottom: 2px; }
  .criteria-card li::before { content: "•"; margin-right: 7px; }
  .curriculum { left: 26px; width: 429px; }
  .behaviour { left: 473px; width: 429px; padding-top: 10px; }

  .tips { left: 0; width: 929px; top: 1043px; text-align: center; font-size: 13.5px; line-height: 1.35; }

  .model {
    left: 26px; top: 1087px; width: 876px; height: 87px; border-radius: 18px;
    padding-top: 12px; text-align: center; font-size: 13.5px; line-height: 1.45;
  }
  .model .card-heading { margin-bottom: 3px; }
</style>
</head>
<body>
  <header>
    <div class="block blue masthead-left"></div>
    <div class="block yellow masthead-right"></div>
    <div class="school-name">Talvin Grove</div>

    <h1 class="block blue title-bar title-main">Talvin Grove Instructional Model</h1>
    <h2 class="block blue title-bar title-sub">Write a powerful Learning Goal &amp; Success Criteria</h2>
  </header>

  <p class="block purpose">Purpose: This poster guides staff to craft clear Learning Goals and Success Criteria aligned to How Talvin Grove Students Learn.</p>
  <p class="block formula-label">Use this one line formula</p>
  <p class="block yellow formula">By the end of the lesson, students will [verb] [skill/concept]*[conditions/context].</p>

  <section class="block yellow rounded card example-left">
    <h3 class="card-heading">Simple example:</h3>
    <p>By the end of the lesson, students will apply Pythagoras theorem to find the hypotenuse of a right triangle with integer side lengths.</p>
  </section>
  <section class="block yellow rounded card example-right">
    <h3 class="card-heading">Second example:</h3>
    <p>By the end of the lesson, students will describe two factors that influence liveability in their local area using evidence from a map.</p>
  </section>

  <h3 class="block blue section-bar essentials-bar">Essentials checklist</h3>
  <ul class="block blue checklist">
    <li>About learning, not tasks: focus on knowledge/skill students will learn today.</li>
    <li>Right verb, right level: choose a precise Bloom’s/cognitive verb. &nbsp;• One idea only: keep scope tight to manage cognitive load.</li>
    <li>Student friendly: plain language students can restate; accessible to all students.</li>
    <li>Visible &amp; revisited: display it; say it at transitions and again during the review at lesson end.</li>
    <li>Assessable: design quick checks and an exit slip that align to the Success Criteria.</li>
    <li>Same Learning Goal for all; differentiate supports (scaffolds/groups), not the intention.</li>
  </ul>

  <h3 class="block yellow section-bar criteria-bar">Success criteria: Curriculum &amp; Behaviour (What / How / Why)</h3>
  <p class="block criteria-intro">Write two short sets of success criteria so students are clear on what they’re learning and how they’ll behave to achieve it and why each matters (aligned with Classroom Profiling).</p>

  <section class="block yellow rounded criteria-card curriculum">
    <h3 class="card-heading">Curriculum (learning):</h3>
    <ul>
      <li>What: the specific knowledge/skill linked to today’s learning goal.</li>
      <li>How: the routine/strategy students will use to demonstrate it (e.g., worked example steps, analysis routine, calculation method).</li>
      <li>Why: the purpose or connection (e.g., links to the next lesson/assessment; helps solve real problems).</li>
    </ul>
  </section>
  <section class="block yellow rounded criteria-card behaviour">
    <h3 class="card-heading">Behaviour (learning behaviours):</h3>
    <ul>
      <li>What: the explicit behaviour expectation (e.g., track the speaker; voice level; hands/signals).</li>
      <li>How: the routine to meet it (e.g., attention signal → pause → response; partner roles; “Ask 3 before me”).</li>
      <li>Why: maximises learning time, safety, and fairness for everyone</li>
    </ul>
  </section>

  <p class="block tips">Keep each bullet student friendly and observable (“I can” statements).<br>Plan a quick check for each “How” and revisit both sets in the review.</p>

  <section class="block yellow model">
    <h3 class="card-heading">Embed the goal in the Talvin Grove Instructional Model</h3>
    <p>Warm up (activate) → I Do → We Do → You Do It Together → You Do → Review goal &amp; success criteria</p>
    <p>• Use evidence from checks to loop back or release (don’t push on if the evidence says pause).</p>
  </section>
</body>
</html>
```